Real Estate Acquisition Company Needs Business Card Design

Tollwyn Real Estate is in need of a business card design!

As a Real Estate Acquisition Company, Tollwyn Real Estate conducts mutually beneficial real estate transactions that actively consider the needs of the seller. At Tollwyn Real Estate we’re actively buying properties from those that see value in a direct transaction, but more importantly want reassurances that they, personally, are in integral part of it. Of course, it all starts with fair market value, but it doesn’t stop there. We’ve found the most success when we offer more. And with our deep experience in this industry, we’ve discovered that we have a lot to offer!

We already have a logo and brand guidelines that we've uploaded. Our final design should stay true to the guidelines. We are looking for a business card design that has two names (Ex. Jane Doe & John Doe) and contact information for each person- this way the company principals can share a card as they often do business as a team.
Updates

The criteria was unfortunately not met on most designs. We are looking for a card that has a layout for TWO names and respective contact information for each of the two people. Almost all designs only had a space for one name and one set of contact information.

Industry/Entity Type

Real Estate

Contact Information for Business Card

We are looking for a business card design that has two names (Ex. Jane Doe & John Doe) and each of their contact information- this way the company principals can share a card as they often do business as a team.

Font styles to use
Other font styles liked:
• Use Brand Guidelines

Requirements
Must have
• Please stay true to our Brand Guidelines for colours, fonts, and positioning of logo.

We require a layout for two names and respective contact information. The company principals work as a team and want a card that has both their information on it.

```html
<!DOCTYPE html>
<html lang="en">
<head>
<meta charset="utf-8">
<title>Tollwyn Real Estate – Business Card</title>
<link href="https://fonts.googleapis.com/css2?family=Montserrat:wght@500;600&family=Open+Sans:wght@400;600&display=swap" rel="stylesheet">
<style>
  :root{
    --navy:#14213a;
    --gold:#f2b544;
    --white:#ffffff;
    --backdrop:#2b2e33;
  }
  *{box-sizing:border-box;margin:0;padding:0}
  html,body{width:1200px;height:900px;overflow:hidden;background:var(--backdrop)}
  .canvas{position:relative;width:1200px;height:900px}
  .card{position:absolute;top:296px;width:540px;height:308px;overflow:hidden;border-radius:3px;box-shadow:0 10px 30px rgba(0,0,0,.35)}
  .card--front{left:40px}
  .card--back{left:620px;background:var(--gold);display:flex;align-items:center;justify-content:center}
  .card__bg{position:absolute;inset:0}
  .brand{display:flex;align-items:center;gap:10px;font-family:"Montserrat",sans-serif;font-weight:600;color:var(--navy);letter-spacing:2px;text-transform:uppercase}
  .brand__dot{width:14px;height:14px;border-radius:50%;background:var(--gold)}
  .card--front .brand{position:absolute;top:42px;right:30px;font-size:24px}
  .card--back .brand{font-size:30px}
  .card--back .brand__dot{background:var(--navy);width:16px;height:16px}
  .contact{position:absolute;top:156px;font-family:"Open Sans",sans-serif;color:var(--white)}
  .contact--one{left:30px}
  .contact--two{left:310px}
  .contact__name{font-family:"Montserrat",sans-serif;font-weight:600;font-size:15px;letter-spacing:1.5px;text-transform:uppercase}
  .contact__title{color:var(--gold);font-size:11px;margin-bottom:10px}
  .contact__row{display:flex;align-items:center;gap:8px;font-size:12px;margin-top:6px}
  .icon{width:18px;height:18px;border:1px solid var(--gold);border-radius:4px;display:flex;align-items:center;justify-content:center}
  .website{position:absolute;left:30px;bottom:22px;font-family:"Open Sans",sans-serif;color:var(--white);font-size:13px;letter-spacing:.5px}
</style>
</head>
<body>
<main class="canvas">
  <section class="card card--front">
    <svg class="card__bg" width="540" height="308" viewBox="0 0 540 308" aria-hidden="true">
      <rect width="540" height="308" fill="var(--navy)"/>
      <polygon points="0,0 540,0 540,150 0,112" fill="var(--white)"/>
      <line x1="0" y1="112" x2="540" y2="150" stroke="var(--gold)" stroke-width="2"/>
      <line x1="272" y1="278" x2="292" y2="168" stroke="var(--gold)" stroke-width="1"/>
    </svg>
    <div class="brand"><span class="brand__dot"></span>Tollwyn Real Estate</div>

    <div class="contact contact--one">
      <p class="contact__name">Devin Harlow</p>
      <p class="contact__title">Director and CEO</p>
      <p class="contact__row"><span class="icon"><svg width="10" height="10" viewBox="0 0 24 24"><path d="M6 2l4 4-2 3c1 3 4 6 7 7l3-2 4 4-3 4C10 22 2 14 2 5z" fill="var(--white)"/></svg></span>+1 555 014 2290</p>
      <p class="contact__row"><span class="icon"><svg width="10" height="8" viewBox="0 0 24 18"><rect x="1" y="1" width="22" height="16" fill="none" stroke="var(--white)" stroke-width="2"/><path d="M1 1l11 9 11-9" fill="none" stroke="var(--white)" stroke-width="2"/></svg></span>devin@tollwynre.com</p>
    </div>

    <div class="contact contact--two">
      <p class="contact__name">Devin Harlow</p>
      <p class="contact__title">Director and CEO</p>
      <p class="contact__row"><span class="icon"><svg width="10" height="10" viewBox="0 0 24 24"><path d="M6 2l4 4-2 3c1 3 4 6 7 7l3-2 4 4-3 4C10 22 2 14 2 5z" fill="var(--white)"/></svg></span>+1 555 014 2290</p>
      <p class="contact__row"><span class="icon"><svg width="10" height="8" viewBox="0 0 24 18"><rect x="1" y="1" width="22" height="16" fill="none" stroke="var(--white)" stroke-width="2"/><path d="M1 1l11 9 11-9" fill="none" stroke="var(--white)" stroke-width="2"/></svg></span>devin@tollwynre.com</p>
    </div>

    <p class="website">www.tollwynre.com</p>
  </section>

  <section class="card card--back">
    <div class="brand"><span class="brand__dot"></span>Tollwyn Real Estate</div>
  </section>
</main>
</body>
</html>
```